Author/ Speaker Business Card design

I need a business card designed that will go with the branding that is already on my book and website. I like clean and straightforward, but I am not opposed to something more 'innovative'.

Target Market(s)

Colleges and Universities, educational institutions

Industry/Entity Type

Education

Contact Information for Business Card

Standard size. It should be able to be printed on good quality white or ivory paper.

Font styles to use
Sans Serif

Colors
0355a3

Requirements
Must have
• There's a blue on my website. It should have some blue. My logo is at the top. It should have the logo incorporated somewhere on it. My name, Author | Speaker | Teacher | Trainer, my phone number (+31 64-207 5819), my email address (milo@theboldlearner.example), Social media icons (twitter, Instagram, LinkedIn) with the addresses (twitter @writermilofenwick, Instagram - theboldlearner, LinkedIn - theboldlearner) By they way, the website is www.theboldlearner.example. There is a photo of the book on the website. Also, my full name is Milo Fenwick
Nice to have
• Try to use the font that is on the website and book. Also, if you could get that blue, that would be great.
Should not have
• My photo

```html
<!DOCTYPE html>
<html lang="en">
<head>
<meta charset="utf-8">
<title>The Bold Learner – Business Card</title>
<link rel="stylesheet" href="https://fonts.googleapis.com/css2?family=Roboto:wght@300;400;500;700&display=swap">
<style>
  :root {
    --card-blue: #0c57a8;
    --ink: #ffffff;
    --backdrop: #e9e7e3;
  }
  * { box-sizing: border-box; margin: 0; padding: 0; }
  html, body { width: 1200px; height: 930px; overflow: hidden; }
  body {
    background: var(--backdrop);
    font-family: "Roboto", sans-serif;
    color: var(--ink);
    position: relative;
  }
  .card {
    position: absolute;
    left: 250px;
    width: 700px;
    height: 400px;
    background: var(--card-blue);
    border-radius: 22px;
  }
  .card--front { top: 50px; }
  .card--back  { top: 480px; }

  .brand-name {
    font-family: "Roboto", sans-serif;
    font-weight: 700;
    color: var(--ink);
    white-space: nowrap;
    display: flex;
    align-items: center;
    gap: 14px;
  }
  .brand-name .brand-dot {
    width: 18px; height: 18px; border-radius: 50%;
    background: var(--ink);
    flex: none;
  }

  /* front */
  .card--front .brand-name {
    position: absolute;
    left: 0; right: 0; top: 150px;
    justify-content: center;
    font-size: 52px;
  }
  .front-web {
    position: absolute;
    left: 0; right: 0; bottom: 44px;
    text-align: center;
    font-size: 17px;
    font-weight: 400;
    letter-spacing: 0.3px;
  }
  .front-web b, .contact-web b { font-weight: 700; }

  /* back */
  .card--back .brand-name {
    position: absolute;
    left: 44px; top: 70px;
    font-size: 38px;
  }
  .person {
    position: absolute;
    right: 44px; top: 72px;
    text-align: right;
  }
  .person-name {
    font-size: 30px;
    font-weight: 500;
    letter-spacing: 0.5px;
    text-transform: uppercase;
  }
  .person-roles {
    font-size: 16px;
    font-weight: 300;
    margin-top: 6px;
  }
  .divider {
    position: absolute;
    left: 44px; right: 44px; top: 200px;
    height: 1.5px;
    background: var(--ink);
  }
  .contacts {
    position: absolute;
    left: 44px; bottom: 40px;
    list-style: none;
    font-size: 17px;
    font-weight: 300;
    line-height: 28px;
  }
  .contacts li, .socials li { display: flex; align-items: center; gap: 12px; }
  .contacts svg { width: 14px; height: 14px; flex: none; }
  .socials {
    position: absolute;
    right: 44px; top: 222px;
    list-style: none;
    font-size: 16px;
    font-weight: 300;
    line-height: 27px;
    text-align: right;
  }
  .socials li { justify-content: flex-end; }
  .social-mark {
    width: 12px; height: 12px; background: var(--ink); border-radius: 50%; flex: none;
  }
</style>
</head>
<body>

  <section class="card card--front">
    <div class="brand-name"><span class="brand-dot"></span>The Bold Learner</div>
    <p class="front-web">www.<b>theboldlearner</b>.example</p>
  </section>

  <section class="card card--back">
    <div class="brand-name"><span class="brand-dot"></span>The Bold Learner</div>

    <div class="person">
      <h1 class="person-name">Milo Fenwick</h1>
      <p class="person-roles">Author | Speaker | Teacher | Trainer</p>
    </div>

    <div class="divider"></div>

    <ul class="socials">
      <li>@writermilofenwick <span class="social-mark"></span></li>
      <li>theboldlearner <span class="social-mark"></span></li>
      <li>theboldlearner <span class="social-mark"></span></li>
    </ul>

    <ul class="contacts">
      <li>
        <svg viewBox="0 0 14 14" aria-hidden="true"><path d="M3 1l2.5 3-1.3 1.5c.8 1.8 2.3 3.3 4.3 4.3L10 8.5l3 2.5-1.5 2C6 13 1 8 1 2.5z" fill="#fff"/></svg>
        (+31 64-207 5819)
      </li>
      <li>
        <svg viewBox="0 0 14 14" aria-hidden="true"><rect x="1" y="3" width="12" height="8" fill="none" stroke="#fff" stroke-width="1.3"/><path d="M1 3l6 5 6-5" fill="none" stroke="#fff" stroke-width="1.3"/></svg>
        info@theboldlearner.example
      </li>
      <li class="contact-web">
        <svg viewBox="0 0 14 14" aria-hidden="true"><circle cx="7" cy="7" r="5.8" fill="none" stroke="#fff" stroke-width="1.2"/><ellipse cx="7" cy="7" rx="2.5" ry="5.8" fill="none" stroke="#fff" stroke-width="1"/><path d="M1.2 7h11.6" stroke="#fff" stroke-width="1"/></svg>
        <span>www.<b>theboldlearner</b>.example</span>
      </li>
    </ul>
  </section>

</body>
</html>
```